Global Expert Network Firm needs business card design

We need business card design for a new company based in Seoul, South Korea called 'Corwell Insight Partners'. We recruit industry experts covering all countries and connect our client and recruited expert by phone, face-to-face meetings and etc. We are a global expert network firm that is focused on delivering high-quality experts to our clients throughout the world. Our clients include multinational corporations, global consulting firms, private equity firms, venture capital firms, asset management companies.
We have made new logo and please find attachment.(Please use new logo)
Target Market(s)
Global Consulting Firms, Investment Firms, Private Equity Firms, Venture Capital Firms.
Industry/Entity Type
Recruitment
Contact Information for Business Card
We need two Languages (English and Korean Version).
The front is Korean and the back is English version.
[The back] [English]
Company Name: Corwell Insight Partners, Inc.
CEO Name: Daniel Park
Address: #507, Hanbit Bldg, 82 Maebongsan-ro, Dobong-gu, Seoul, 01327, Korea
Tel. +82 2 718 4052
Fax. +82 2 864 1097
Mobile. +82 10 7264 8815
Email: daniel@corwellip.com
Web: www.corwellip.com
[The front] [Korean] => Described in same order as English version.
회사명: 코웰인사이트파트너스(주)
대표이사: 박도현
주소: 서울시 도봉구 매봉산로 82 한빛빌딩 507호
Tel. 02 718 4052
Fax. 02 864 1097
Mobile. 010 7264 8815
Web: www.corwellip.com
Look and feel
Each slider illustrates characteristics of the customer's brand and the style your logo design should communicate.

```html
<!DOCTYPE html>
<html lang="en">
<head>
<meta charset="utf-8">
<title>Corwell Insight Partners — Business Cards</title>
<link rel="stylesheet" href="https://fonts.googleapis.com/css2?family=Noto+Sans+KR:wght@400;500;700&display=swap">
<style>
  :root {
    --navy: #1c2163;
    --navy-deep: #141850;
    --ink: #3a3a44;
    --rule: #8a8cb0;
    --paper: #ffffff;
    --wave-shade: #d9dae3;
    --backdrop: #4a4a4c;
  }
  * { box-sizing: border-box; margin: 0; padding: 0; }
  html, body { width: 1200px; height: 1200px; overflow: hidden; }
  body {
    background: var(--backdrop);
    font-family: "Noto Sans KR", "Open Sans", sans-serif;
    color: var(--ink);
    position: relative;
  }
  .card {
    position: absolute;
    left: 170px;
    width: 860px;
    height: 490px;
    background: var(--paper);
    overflow: hidden;
    box-shadow: 0 14px 30px rgba(0,0,0,0.35);
  }
  .card--front { top: 70px; }
  .card--back { top: 640px; }
  .card__wave { position: absolute; inset: 0; width: 100%; height: 100%; }
  .brand {
    position: absolute;
    left: 60px;
    top: 48px;
    color: var(--paper);
    font-weight: 400;
    font-size: 34px;
    line-height: 1.18;
    letter-spacing: 0.06em;
    text-transform: uppercase;
  }
  .brand__suffix { font-size: 20px; letter-spacing: 0.02em; text-transform: none; }
  .contact {
    position: absolute;
    right: 56px;
    top: 252px;
    width: 620px;
    text-align: right;
  }
  .contact__name {
    color: var(--navy);
    font-size: 34px;
    line-height: 1.1;
  }
  .card--back .contact__name { font-weight: 700; letter-spacing: 0.02em; }
  .card--front .contact__name { font-weight: 400; font-size: 38px; }
  .contact__title {
    margin-top: 6px;
    font-size: 21px;
    display: flex;
    justify-content: flex-end;
    align-items: center;
    gap: 8px;
  }
  .contact__title .sep { color: var(--rule); }
  .contact__grid {
    margin-top: 8px;
    display: flex;
    justify-content: flex-end;
    font-size: 21px;
    line-height: 1.5;
  }
  .contact__col { padding: 0 16px; }
  .contact__col + .contact__col { border-left: 1px solid var(--rule); padding-right: 0; }
  .contact__line { display: flex; align-items: center; justify-content: flex-end; gap: 8px; white-space: nowrap; }
  .icon { width: 18px; height: 18px; flex: none; fill: var(--navy); }
  .address {
    margin-top: 12px;
    padding-top: 8px;
    border-top: 1px solid var(--rule);
    font-size: 19px;
    text-align: left;
    white-space: nowrap;
  }
</style>
</head>
<body>

<svg width="0" height="0" style="position:absolute" aria-hidden="true">
  <defs>
    <symbol id="i-mobile" viewBox="0 0 16 16"><rect x="4" y="1" width="8" height="14" rx="1.5"/><rect x="5.5" y="3" width="5" height="7" fill="#fff"/></symbol>
    <symbol id="i-phone" viewBox="0 0 16 16"><path d="M1 6c0-2 3-3 7-3s7 1 7 3v1h-3.5V5.5h-7V7H1z"/><path d="M3 8h10l1 6H2z"/><circle cx="8" cy="11" r="1.6" fill="#fff"/></symbol>
    <symbol id="i-fax" viewBox="0 0 16 16"><rect x="5" y="1" width="6" height="6" fill="none" stroke="#1c2163" stroke-width="1.3"/><rect x="2" y="7" width="12" height="7" rx="1"/><rect x="4" y="9" width="8" height="1.4" fill="#fff"/></symbol>
    <symbol id="i-globe" viewBox="0 0 16 16"><circle cx="8" cy="8" r="7"/><g fill="none" stroke="#fff" stroke-width="1"><ellipse cx="8" cy="8" rx="3" ry="7"/><path d="M1 8h14M2.2 4.5h11.6M2.2 11.5h11.6"/></g></symbol>
    <symbol id="i-mail" viewBox="0 0 16 16"><rect x="1" y="3" width="14" height="10"/><path d="M1 3l7 6 7-6" fill="none" stroke="#fff" stroke-width="1.2"/></symbol>
    <linearGradient id="navy-fill" x1="0" y1="0" x2="1" y2="1">
      <stop offset="0" stop-color="#141850"/>
      <stop offset="1" stop-color="#232a70"/>
    </linearGradient>
  </defs>
</svg>

<!-- Korean side -->
<section class="card card--front" lang="ko">
  <svg class="card__wave" viewBox="0 0 860 490" preserveAspectRatio="none" aria-hidden="true">
    <path d="M0 0H660C600 50 520 170 400 205C290 238 140 215 0 300Z" fill="var(--wave-shade)" transform="translate(0 10)"/>
    <path d="M0 0H660C600 50 520 170 400 205C290 238 140 215 0 300Z" fill="url(#navy-fill)"/>
  </svg>
  <div class="brand">Corwell<br>Insight<br>Partners <span class="brand__suffix">Inc.</span></div>
  <div class="contact">
    <div class="contact__name">박도현</div>
    <div class="contact__title">대표이사 <span class="sep">|</span><svg class="icon"><use href="#i-mobile"/></svg> +82 10 7264 8815</div>
    <div class="contact__grid">
      <div class="contact__col">
        <div class="contact__line">www.corwellip.com <svg class="icon"><use href="#i-globe"/></svg></div>
        <div class="contact__line">daniel@corwellip.com <svg class="icon"><use href="#i-mail"/></svg></div>
      </div>
      <div class="contact__col">
        <div class="contact__line">+82 2 718 4052 <svg class="icon"><use href="#i-phone"/></svg></div>
        <div class="contact__line">+82 2 864 1097 <svg class="icon"><use href="#i-fax"/></svg></div>
      </div>
    </div>
    <div class="address">서울시 도봉구 매봉산로 82 한빛빌딩 507호</div>
  </div>
</section>

<!-- English side -->
<section class="card card--back" lang="en">
  <svg class="card__wave" viewBox="0 0 860 490" preserveAspectRatio="none" aria-hidden="true">
    <path d="M0 0H660C600 50 520 170 400 205C290 238 140 215 0 300Z" fill="var(--wave-shade)" transform="translate(0 10)"/>
    <path d="M0 0H660C600 50 520 170 400 205C290 238 140 215 0 300Z" fill="url(#navy-fill)"/>
  </svg>
  <div class="brand">Corwell<br>Insight<br>Partners <span class="brand__suffix">Inc.</span></div>
  <div class="contact">
    <div class="contact__name">DANIEL PARK</div>
    <div class="contact__title">CEO <span class="sep">|</span><svg class="icon"><use href="#i-mobile"/></svg> +82 10 7264 8815</div>
    <div class="contact__grid">
      <div class="contact__col">
        <div class="contact__line">www.corwellip.com <svg class="icon"><use href="#i-globe"/></svg></div>
        <div class="contact__line">daniel@corwellip.com <svg class="icon"><use href="#i-mail"/></svg></div>
      </div>
      <div class="contact__col">
        <div class="contact__line">+82 2 718 4052 <svg class="icon"><use href="#i-phone"/></svg></div>
        <div class="contact__line">+82 2 864 1097 <svg class="icon"><use href="#i-fax"/></svg></div>
      </div>
    </div>
    <div class="address">#507, Hanbit Bldg, 82 Maebongsan-ro, Dobong-gu, Seoul, 01327, Korea</div>
  </div>
</section>

</body>
</html>
```